We are opening a new restaurant concept called Lanternleaf - Fresh Asian Cuisine. Will be a trendy, casual dining restaurant (somewhat similar to a QR Morvins).
I have included pics of our logo in different formats and a picture of our front menu cover and inside menu as well as our actual menu in draft format. Need 6 individual pages total and letter size. Inside cover would be a "about us" type page that describes who we are and mission statement of restaurant (script unwritten at this time), Next page would be appetizers, inside page would have entrees on left and right side of book, then noodles/rice, vegetarian, kids and dessert section, last page would be drink/cocktail menu (still in progress).

```html
<!DOCTYPE html>
<html lang="en">
<head>
<meta charset="utf-8">
<title>Lanternleaf - Fresh Asian Cuisine Menu</title>
<link href="https://fonts.googleapis.com/css2?family=Oswald:wght@500;600&family=Jost:wght@400;500;700&display=swap" rel="stylesheet">
<style>
:root{
  --ink:#1a1a1a;
  --muted:#444;
  --red:#d0202a;
  --band-dark:#7a0c12;
  --band-mid:#b3161e;
  --band-light:#d42a32;
  --rule-dark:#222;
  --rule-gray:#8a8a8a;
  --paper:#ffffff;
  --stage:#000000;
}
*{margin:0;padding:0;box-sizing:border-box}
html,body{width:1200px;height:1200px;overflow:hidden;background:var(--stage)}
.spread{position:relative;width:1200px;height:1200px;overflow:hidden;background:var(--stage);font-family:"Jost",sans-serif;color:var(--ink)}
.page{position:absolute;background:var(--paper);overflow:hidden}
.band{position:absolute;left:0;top:0;width:100%;height:88px;
  background:linear-gradient(135deg,var(--band-dark),var(--band-mid) 30%,var(--band-light) 50%,var(--band-mid) 70%,var(--band-dark));
  border-bottom:3px solid var(--rule-dark);box-shadow:0 3px 0 var(--rule-gray)}
.section-title{position:absolute;font-family:"Oswald",sans-serif;font-weight:600;color:var(--red);
  font-size:22px;letter-spacing:3px;line-height:1;transform:translateX(-50%);white-space:nowrap}
.sub-title{position:absolute;font-family:"Oswald",sans-serif;font-weight:500;color:var(--ink);
  font-size:15px;letter-spacing:2px;line-height:1;transform:translateX(-50%);white-space:nowrap}
.items{position:absolute;list-style:none}
.item{margin-bottom:20px}
.item-name{font-weight:500;font-size:12.5px;line-height:16px;white-space:nowrap}
.item-desc{font-size:11px;line-height:11.5px;color:var(--muted);white-space:nowrap}
.kids .item{margin-bottom:25px}

.cover{left:0;top:0;width:588px;height:760px}
.entrees-back{left:674px;top:0;width:526px;height:400px}
.entrees-left{left:612px;top:150px;width:588px;height:600px}
.entrees-right{left:674px;top:306px;width:526px;height:762px}
.appetizers{left:24px;top:306px;width:588px;height:762px}
.noodles{left:399px;top:428px;width:597px;height:772px}

.brand{position:absolute;left:120px;top:112px;display:flex;align-items:center;gap:12px}
.brand-dot{width:44px;height:44px;border-radius:50%;background:var(--red)}
.brand-text{font-weight:700;color:var(--ink);line-height:1}
.brand-name{font-size:44px;letter-spacing:-1px;display:block}
.brand-tag{font-size:12px;letter-spacing:3px;display:block;margin-top:6px;text-align:right}
.intro{position:absolute;left:121px;top:250px;width:320px;font-size:10.5px;line-height:11.5px;color:var(--ink)}
.intro p{margin-bottom:7px}
</style>
</head>
<body>
<main class="spread">

  <section class="page cover">
    <div class="band" role="img" aria-label="Red woven basket texture band"></div>
    <div class="brand">
      <span class="brand-dot"></span>
      <span class="brand-text">
        <span class="brand-name">LANTERNLEAF</span>
        <span class="brand-tag">FRESH ASIAN CUISINE</span>
      </span>
    </div>
    <div class="intro">
      <p>Uscia soluptae ernam des eos et et excerite voluptat laborpost aute pellaut facipsant quiasseria nosamet od evelit aut la sincit, quiae rest molesedis et vercili quiatem duntur, tem. Ut everferatur sum quaspicium qui tectat volupti urepreh enienientem vent.</p>
      <p>Sed milibusam, aut que nimincipis atate porpore ssimin prorrum latem.</p>
    </div>
  </section>

  <section class="page entrees-back">
    <div class="band" role="img" aria-label="Red woven basket texture band"></div>
  </section>

  <section class="page entrees-left">
    <div class="band" role="img" aria-label="Red woven basket texture band"></div>
    <h2 class="section-title" style="left:294px;top:114px">ENTREES</h2>
    <ul class="items" style="left:34px;top:194px;width:240px">
      <li class="item"><div class="item-name">Kung Pao Chicken $14</div><div class="item-desc">Chicken wok tossed with peanuts, dried<br>red chili and scallions in a savory<br>sauce</div></li>
      <li class="item"><div class="item-name">Orange Chicken $14</div></li>
    </ul>
  </section>

  <section class="page entrees-right">
    <div class="band" role="img" aria-label="Red woven basket texture band"></div>
    <h2 class="section-title" style="left:294px;top:114px">ENTREES</h2>
    <h3 class="sub-title" style="left:428px;top:166px">BEEF &amp; PORK</h3>
    <ul class="items" style="left:306px;top:194px;width:300px">
      <li class="item"><div class="item-name">Dancing Beef $16</div><div class="item-desc">Angus Beef Sirloin slices on a bed of sizzling rice<br>crackers, black peppercorn and Thai chili</div></li>
      <li class="item"><div class="item-name">Oyster Beef $14</div><div class="item-desc">Tender cuts of steak wok fried and marinated in<br>homemade oyster sauce</div></li>
      <li class="item"><div class="item-name">Double Pepper Beef $16</div><div class="item-desc">Beef Skirt Steak cubes with fresh green peppers,<br>Thai chili, Serrano Pepper and celery</div></li>
      <li class="item"><div class="item-name">Sweet &amp; Sour Baby Back Ribs $16</div><div class="item-desc">Tender Baby back ribs in sweet and sour sauce</div></li>
      <li class="item"><div class="item-name">Dancing Pork Belly $15</div><div class="item-desc">Braised Pork Belly on sizzling rice cracker</div></li>
      <li class="item"><div class="item-name">Twice Cooked Pork $14</div><div class="item-desc">Stir fried Pork Belly slices with leek and fermented<br>black beans</div></li>
    </ul>
  </section>

  <section class="page appetizers">
    <div class="band" role="img" aria-label="Red woven basket texture band"></div>
    <h2 class="section-title" style="left:289px;top:114px">APPETIZERS</h2>
    <ul class="items" style="left:35px;top:161px;width:250px">
      <li class="item"><div class="item-name">Edamame $4</div><div class="item-desc">Seasoned &amp; boiled soy bean</div></li>
      <li class="item"><div class="item-name">Scallion Pancakes $6</div><div class="item-desc">Traditional Chinese flatbread folded with oil and<br>minced scallions and pan fried</div></li>
      <li class="item"><div class="item-name">Lanternleaf Lettuce Wraps $8</div><div class="item-desc">Seasoned ground chicken wrapped in lettuce and<br>drizzled with our secret sauce</div></li>
      <li class="item"><div class="item-name">Salt &amp; Pepper Calamari $9</div><div class="item-desc">Crispy Calamari with Green &amp; red peppers and<br>onions</div></li>
      <li class="item"><div class="item-name">Singapore Ribs $9</div><div class="item-desc">Tender baby back ribs in a sweet homemade glaze</div></li>
      <li class="item"><div class="item-name">Spicy Bang Bang Shrimp $9</div><div class="item-desc">Crispy fried shrimp tossed in our creamy spicy sauce</div></li>
      <li class="item"><div class="item-name">Drunken Chicken $8</div><div class="item-desc">Chicken, Thai chili and a house made spicy sauce</div></li>
      <li class="item"><div class="item-name">Sichuan Spiced Beef $9</div><div class="item-desc">Beef Shank, beef tripe, cilantro, peanuts and celery</div></li>
      <li class="item"><div class="item-name">Beef Crispy Bottom Bow $10</div><div class="item-desc">Pan fried crispy bottom Bao, stuffed with beef,<br>drizzled with scallion and sesame</div></li>
    </ul>
    <ul class="items" style="left:300px;top:161px;width:250px">
      <li class="item"><div class="item-name">Crispy Mala Beef $10</div><div class="item-desc">Dry fried shredded beef with chili<br>peppers, garlic, scallion and Sichuan<br>peppercorn oil</div></li>
      <li class="item"><div class="item-name">Steamed Chicken Dumplings $8</div><div class="item-desc">Chinese dumplings with chicken,<br>mushrooms and scallion</div></li>
      <li class="item"><div class="item-name">Red Oil Dumplings $8</div><div class="item-desc">Pork filled dumplings in red chili oil<br>with sesame</div></li>
      <li class="item"><div class="item-name">Pork Egg Rolls $6</div><div class="item-desc">Hand rolled with pork and cabbage,<br>sour mustard sauce</div></li>
      <li class="item"><div class="item-name">Vegetarian Spring Rolls $6</div><div class="item-desc">Fresh rice paper rolls with bean<br>sprouts and lettuce</div></li>
      <li class="item"><div class="item-name">Garlic Cucumber $5</div><div class="item-desc">Sliced cucumber in garlic sauce</div></li>
      <li class="item"><div class="item-name">Lanternleaf House Soup $6</div><div class="item-desc">Tangy broth with chili, mushroom,<br>tofu, egg and cabbage</div></li>
      <li class="item"><div class="item-name">West Lake Soup $6</div><div class="item-desc">Light creamy soup with beef,<br>mushroom, tofu, egg white and<br>cilantro</div></li>
    </ul>
  </section>

  <section class="page noodles">
    <div class="band" role="img" aria-label="Red woven basket texture band"></div>
    <h2 class="section-title" style="left:161px;top:113px">NOODLES &amp; RICE</h2>
    <h2 class="section-title" style="left:436px;top:113px">VEGETARIAN DISHES</h2>
    <ul class="items" style="left:35px;top:156px;width:260px">
      <li class="item"><div class="item-name">Lanternleaf's Fried Rice $12</div><div class="item-desc">Shrimp, chicken, and beef, farm fresh eggs, onions,<br>and scallions</div></li>
      <li class="item"><div class="item-name">Vegetarian White Fried Rice $10</div><div class="item-desc">Mixed vegetables with jasmine rice</div></li>
      <li class="item"><div class="item-name">Lanternleaf's Lo Mein $12</div><div class="item-desc">Shrimp, chicken, and beef, farm fresh eggs, onions,<br>and scallions</div></li>
      <li class="item"><div class="item-name">Vegetarian Lo Mein $10</div><div class="item-desc">Mixed vegetables with jasmine rice</div></li>
    </ul>
    <h2 class="section-title" style="left:161px;top:407px">DESSERT</h2>
    <ul class="items" style="left:35px;top:448px;width:260px">
      <li class="item"><div class="item-name">The Great Wall of Cake $7</div><div class="item-desc">Scale this fortress of Chocolate Cake Delight.</div></li>
      <li class="item"><div class="item-name">Cheesecake Wontons (4) $6</div><div class="item-desc">Fried wontons stuffed with cheesecake and dipped<br>in raspberry sauce</div></li>
      <li class="item"><div class="item-name">Tempura Snowball $4</div><div class="item-desc">Vanilla ice cream fried in tempura batter with<br>powdered sugar and fudge</div></li>
      <li class="item"><div class="item-name">Sweet Rice Patties in Caramel $7</div><div class="item-desc">Traditional Chinese dessert with sweet rice dipped in<br>a caramel sauce</div></li>
    </ul>
    <ul class="items" style="left:310px;top:156px;width:260px">
      <li class="item"><div class="item-name">Wok Tossed String Beans $9</div><div class="item-desc">Fresh string beans mixed with pickled vegetables</div></li>
      <li class="item"><div class="item-name">Mapo Tofu $11</div><div class="item-desc">Soft Tofu, scallion, Sichuan peppercorn and peppers</div></li>
      <li class="item"><div class="item-name">Spicy Garlic Eggplant $12</div><div class="item-desc">Chinese eggplant in spicy garlic sauce drizzled with<br>scallions</div></li>
      <li class="item"><div class="item-name">Buddha's Delight $10</div><div class="item-desc">Seasonal vegetables wok-tossed in our light soy<br>garlic sauce</div></li>
      <li class="item"><div class="item-name">Stir-fried Eggplant Beans $12</div><div class="item-desc">Chinese eggplant with sautéed green beans</div></li>
      <li class="item"><div class="item-name">Shiitake Baby Bok-Choy $12</div><div class="item-desc">Sautéed baby bok-choy with Shiitake mushrooms in<br>brown sauce</div></li>
    </ul>
    <h2 class="section-title" style="left:436px;top:510px">KIDS MENU</h2>
    <ul class="items kids" style="left:310px;top:552px;width:260px">
      <li class="item"><div class="item-name">Beef Lo Mein $5</div><div class="item-desc">Lo Mein noodles mixed with beef in garlic sauce</div></li>
      <li class="item"><div class="item-name">Chicken Fried Rice $5</div><div class="item-desc">Fried rice, farm fresh eggs, onions, and scallions</div></li>
      <li class="item"><div class="item-name">Sweet &amp; Sour Chicken $6</div><div class="item-desc">Bite sized crispy chicken with sweet &amp; sour sauce</div></li>
      <li class="item"><div class="item-name">Lemon Chicken $6</div><div class="item-desc">Bite sized crispy chicken in a sweet lemon sauce</div></li>
    </ul>
  </section>

</main>
</body>
</html>
```